Advanced Therapeutic Massage Therapist

I need a business card advertising my massage services as an advanced therapeutic massage therapist. I offer advanced therapeutic massage, swedish and deep tissue. I want to create a simple, professional and feminine card. I like bright colours and creativity.

I prefer a bold and experimental approach rather than something status-quo. A card to suggest therapeutic healing through dynamic massage. Motifs, shapes or layout which suggest movement and flow.
Updates

Target Market(s)

Everybody!

Industry/Entity Type

Health And Wellness

Contact Information for Business Card

The card should include:
My name, logo, services offered and my contact details.

Aoibhín Delaney
Massage Therapist

- Swedish - Deep Tissue - Advanced Therapeutic

Phone: (+353) 87 261 9043
Email: regenerate@aoibhindelaney-example.com
Website: www.aoibhindelany-example.com

Font styles to use
Serif
Sans Serif
Decorative
Script

Colors

Designer to choose colors to be used in the design.

Requirements
Must have
• An example may contain something like this, yet concise:
• "Aoibhín Delaney
• Massage Therapist
• - Swedish - Deep Tissue - Advanced Therapeutic"
Nice to have
• This sentence is optional:
• Imagery such as a logo or symbol. I have attached a file containing a logo I had produced however the name is incorrect now as it is "Aoibhín" not "Evie". It could be edited to change it to Aoibhín.
• I have sent the file as .psd .jpg. .pdf and .png
• I like when the card conveys energy, movement, pressure points, flow etc.
• I just like the designer to follow their own style and ideas. I like bright colours but must have a lot of a base colour to offset it. I really prefer them to follow their own inspiration. That is my preference.
Should not have
• Pine trees, non-native trees to Britain and Ireland, exotic flowers or animals that are not native to Britain and Ireland.
• I don't like brown as the background colour of the card.
• The cars shouldn't look like a wedding invitation i.e too many floral type designs.

```html
<!DOCTYPE html>
<html lang="en">
<head>
<meta charset="utf-8">
<title>Aoibhín Delaney – Massage Therapist Business Card</title>
<link rel="stylesheet" href="https://fonts.googleapis.com/css2?family=Source+Sans+3:wght@400;600;700&display=swap">
<style>
  :root {
    --backdrop: #e9e7e4;
    --card-white: #fbfbfa;
    --card-black: #1b1c1d;
    --ink: #2a2a2a;
    --gold: #b88a3a;
    --gold-light: #d9b46a;
    --mint: #bfe6da;
    --mint-deep: #9fd3c6;
    --bullet: #c9c2ae;
  }
  * { box-sizing: border-box; margin: 0; padding: 0; }
  html, body {
    width: 1200px; height: 844px; overflow: hidden;
    background: var(--backdrop);
    font-family: "Source Sans 3", "Myriad Pro", sans-serif;
  }
  .stage {
    width: 1200px; height: 844px;
    display: flex; align-items: center; justify-content: center; gap: 50px;
  }
  .card {
    position: relative;
    width: 525px; height: 300px;
    box-shadow: 0 6px 18px rgba(0,0,0,.18);
  }
  .card--front { background: var(--card-white); }
  .card--back { background: var(--card-black); }

  .emblem {
    position: absolute;
    display: flex; flex-direction: column; align-items: center; gap: 8px;
  }
  .card--front .emblem { top: 34px; right: 52px; }
  .card--back .emblem { top: 50%; left: 50%; transform: translate(-50%, -50%); }
  .emblem__disc {
    width: 130px; height: 130px; border-radius: 50%;
    background: radial-gradient(circle at 45% 40%, var(--mint), var(--mint-deep));
    box-shadow: 0 0 0 4px var(--gold-light);
  }
  .emblem__name {
    font-size: 12px; font-weight: 600; color: var(--gold);
    letter-spacing: .04em;
  }

  .details {
    position: absolute; left: 34px; bottom: 28px;
    color: var(--ink);
  }
  .details__name {
    font-size: 21px; font-weight: 700; color: var(--gold);
    line-height: 1.05;
  }
  .details__role { font-size: 14.5px; margin-bottom: 16px; }
  .contact { list-style: none; font-size: 14px; line-height: 1.5; margin-bottom: 14px; }
  .contact li { display: flex; align-items: center; gap: 8px; }
  .contact svg { width: 12px; height: 12px; fill: var(--gold); flex: none; }
  .services {
    list-style: none; font-size: 15px; font-weight: 700;
    display: flex; flex-wrap: wrap; width: 210px; column-gap: 4px; line-height: 1.45;
  }
  .services li { display: flex; align-items: center; gap: 5px; }
  .services li::before {
    content: ""; width: 9px; height: 9px; border-radius: 50%;
    background: radial-gradient(circle at 35% 35%, #eef3ea, var(--bullet));
  }
</style>
</head>
<body>
<main class="stage">
  <section class="card card--front" aria-label="Card front">
    <div class="emblem">
      <div class="emblem__disc" role="img" aria-label="Circular brand emblem in mint and gold"></div>
      <span class="emblem__name">Aoibhín Delaney</span>
    </div>
    <div class="details">
      <h1 class="details__name">Aoibhín Delaney</h1>
      <p class="details__role">Massage Therapist</p>
      <ul class="contact">
        <li>
          <svg viewBox="0 0 24 24" aria-hidden="true"><path d="M6.6 10.8a15 15 0 0 0 6.6 6.6l2.2-2.2c.3-.3.7-.4 1-.2 1.1.4 2.3.6 3.6.6.6 0 1 .4 1 1V20c0 .6-.4 1-1 1A17 17 0 0 1 3 4c0-.6.4-1 1-1h3.5c.6 0 1 .4 1 1 0 1.3.2 2.5.6 3.6.1.3 0 .7-.2 1z"/></svg>
          (+353) 87 261 9043
        </li>
        <li>
          <svg viewBox="0 0 24 24" aria-hidden="true"><path d="M2 5h20v14H2zm2 2v.5l8 5 8-5V7l-8 5z"/></svg>
          aoibhinmassage@example-mail.com
        </li>
      </ul>
      <ul class="services">
        <li>Swedish</li>
        <li>Deep Tissue</li>
        <li>Advanced Therapeutic</li>
      </ul>
    </div>
  </section>

  <section class="card card--back" aria-label="Card back">
    <div class="emblem">
      <div class="emblem__disc" role="img" aria-label="Circular brand emblem in mint and gold"></div>
      <span class="emblem__name">Aoibhín Delaney</span>
    </div>
  </section>
</main>
</body>
</html>
```